Global Parking App needs sleek business cards developed

We need a business card design for a soon-to-be launched global parking app called Vantle(TM). We need a sleek business card which ties in with the brand and existing logo.

We would like to see a designs that use the colors black and white. The final design should communicate the idea of 'cool'+'attitude'.

Business Card should contain the following:

FRONT

1. Logo and Strapline

Vantle(TM)
Your private parking space

2. Contact details

Lewis Hartigan
Managing Director
Vantle Technologies Pty Ltd
M: (+61)(0)417382916
E: lewis@vantle.example
W: www.vantle.example

BACK

The future of parking has arrived...

Same-style icons in a line of

1. a car
2. a motorbike/scooter
3. a boat
4. helicopter

Try Vantle(TM) today > (App Store logos, see attached)

www.vantle.example

```html
<!DOCTYPE html>
<html lang="en">
<head>
<meta charset="utf-8">
<title>Vantle business cards</title>
<link rel="stylesheet" href="https://fonts.googleapis.com/css2?family=Arimo:wght@400;700&display=swap">
<style>
  :root {
    --ink: #0b0b0b;
    --paper: #ffffff;
    --stage: #e7e7e5;
    --grey: #8a8a8a;
    --mid: #444444;
  }
  * { margin: 0; padding: 0; box-sizing: border-box; }
  html, body { width: 1200px; height: 902px; overflow: hidden; }
  body {
    background: var(--stage);
    font-family: "Arimo", Arial, sans-serif;
    color: var(--ink);
    position: relative;
  }
  .card {
    position: absolute;
    left: 250px;
    width: 700px;
    height: 400px;
    background: var(--paper);
    overflow: hidden;
    box-shadow: 0 6px 18px rgba(0,0,0,.18);
  }
  .card--back { top: 40px; }
  .card--front { top: 470px; }

  /* back */
  .headline {
    position: absolute; left: 0; right: 0; top: 44px; text-align: center;
    font-size: 40px; font-weight: 700; letter-spacing: -0.3px;
  }
  .back-url {
    position: absolute; left: 0; right: 0; top: 104px; text-align: center;
    font-size: 22px; color: var(--mid); letter-spacing: 0.5px;
  }
  .vehicle-row {
    position: absolute; left: 48px; right: 48px; top: 170px;
    display: flex; justify-content: space-between;
  }
  .vehicle-tile {
    width: 128px; height: 96px; background: var(--ink); border-radius: 3px;
  }
  .store-badge {
    position: absolute; left: 295px; top: 310px;
    width: 110px; height: 40px; border-radius: 7px; background: var(--ink);
  }

  /* front */
  .swoosh { position: absolute; inset: 0; }
  .brand {
    position: absolute; left: 40px; top: 56px; width: 280px;
    display: flex; flex-direction: column; align-items: center;
  }
  .brand-square {
    width: 150px; height: 150px; background: var(--ink); border-radius: 14px;
  }
  .brand-name {
    margin-top: 22px; font-size: 44px; font-weight: 400; letter-spacing: 14px;
    padding-left: 14px;
  }
  .brand-name sup { font-size: 14px; letter-spacing: 0; vertical-align: 26px; }
  .strapline {
    margin-top: 10px; font-size: 20px; font-weight: 700; color: var(--mid);
  }
  .person {
    position: absolute; right: 40px; top: 24px; text-align: right;
  }
  .person-name { font-size: 40px; font-weight: 700; letter-spacing: -0.5px; }
  .person-role, .person-company { font-size: 20px; color: var(--mid); margin-top: 4px; }
  .contact {
    position: absolute; right: 40px; top: 262px; list-style: none;
    color: var(--paper); font-size: 19px; text-align: right;
  }
  .contact li { display: flex; align-items: center; justify-content: flex-end; gap: 12px; margin-bottom: 9px; }
  .contact-icon { width: 18px; height: 18px; }
</style>
</head>
<body>

<section class="card card--back" aria-label="Card back">
  <h2 class="headline">The future of parking has arrived</h2>
  <p class="back-url">www.vantle.example</p>
  <div class="vehicle-row">
    <div class="vehicle-tile" role="img" aria-label="Car icon"></div>
    <div class="vehicle-tile" role="img" aria-label="Motorbike icon"></div>
    <div class="vehicle-tile" role="img" aria-label="Sailing boat icon"></div>
    <div class="vehicle-tile" role="img" aria-label="Helicopter icon"></div>
  </div>
  <div class="store-badge" role="img" aria-label="App store badge"></div>
</section>

<section class="card card--front" aria-label="Card front">
  <svg class="swoosh" viewBox="0 0 700 400" preserveAspectRatio="none" aria-hidden="true">
    <path d="M300 400 C 420 250, 520 165, 700 150 L700 400 Z" fill="var(--grey)"/>
    <path d="M318 400 C 435 262, 535 180, 700 166 L700 400 Z" fill="var(--ink)"/>
  </svg>

  <div class="brand">
    <div class="brand-square"></div>
    <div class="brand-name">VANTLE<sup>™</sup></div>
    <div class="strapline">Your private parking space</div>
  </div>

  <div class="person">
    <div class="person-name">Lewis Hartigan</div>
    <div class="person-role">Managing Director</div>
    <div class="person-company">Vantle Technologies Pty Ltd</div>
  </div>

  <ul class="contact">
    <li>(+61)(0)417382916
      <svg class="contact-icon" viewBox="0 0 18 18" aria-hidden="true"><rect width="18" height="18" rx="2" fill="#fff"/><path d="M5 4h3l1 3-2 1a7 7 0 0 0 3 3l1-2 3 1v3c-6 0-9-3-9-9z" fill="#000"/></svg>
    </li>
    <li>lewis@vantle.example
      <svg class="contact-icon" viewBox="0 0 18 18" aria-hidden="true"><rect width="18" height="18" rx="2" fill="#fff"/><rect x="3" y="5" width="12" height="8" fill="none" stroke="#000" stroke-width="1.4"/><path d="M3 5l6 5 6-5" fill="none" stroke="#000" stroke-width="1.4"/></svg>
    </li>
    <li>www.vantle.example
      <svg class="contact-icon" viewBox="0 0 18 18" aria-hidden="true"><rect width="18" height="18" rx="2" fill="#fff"/><circle cx="9" cy="9" r="5.5" fill="none" stroke="#000" stroke-width="1.4"/><path d="M3.5 9h11M9 3.5c-3 3-3 8 0 11M9 3.5c3 3 3 8 0 11" fill="none" stroke="#000" stroke-width="1.1"/></svg>
    </li>
  </ul>
</section>

</body>
</html>
```